Quarvena Broadband Services TRPL - New Service

This will be an TRPL Mailer promoting internet services

We will be using the 8.5" x 11" TRPL Printing option at

nextdayflyershttps://www.pressloomcards.com/postcard-printing/whole-route-bulk-post

We want to introduce people who have not signed up to our services and let them know what makes us different from out customers.

We offer:

24/7 Technical Support
Flat monthly rates
No data caps
No speed throttling
No long term contracts
No installation fees
Internet Plans start at $39.95/mo

Target Market(s)

Homeowners seeking internet service

Industry/Entity Type

Internet Service Provider

Font styles to use
Other font styles liked:
• RockoFLF

Colors

Designer to choose colors to be used in the design.

Requirements
Must have
• Our logo, website and phone number
• www.quarvena.co
• 555-304-8926
• We want to introduce people to our services with something like "Quarvena Broadband Services are available in your area"
Nice to have
• Our font is called RockoFLF (not a must have if you think something else looks better)
Should not have
• Do not deviate far from our normal color scheme, I would look at our website to get a feel for the colors we use. Usually that blue color
• We do not like cartoonish, I would use stock photos with people using laptops or something
• We have attached an example of a door hanger we have done in the past to show the feel of advertising we like, don't just copy it

```html
<!DOCTYPE html>
<html lang="en">
<head>
<meta charset="utf-8">
<title>Quarvena Broadband Services – Mailer</title>
<link rel="stylesheet" href="https://fonts.googleapis.com/css2?family=Fredoka:wght@500;600&family=Roboto:wght@400&family=Arimo:wght@400;700&display=swap">
<style>
  :root {
    --ink: #262527;
    --brand-blue: #1b86d1;
    --paper: #ffffff;
    --text: #1c1c1c;
  }
  * { margin: 0; padding: 0; box-sizing: border-box; }
  html, body { width: 934px; height: 1200px; overflow: hidden; background: var(--paper); }
  .mailer { position: relative; width: 934px; height: 1200px; background: var(--paper); font-family: "Roboto", sans-serif; color: var(--text); }

  .masthead { position: absolute; left: 0; top: 0; width: 934px; height: 188px; background: var(--ink); }
  .brand { position: absolute; left: 52px; top: 66px; display: flex; align-items: center; gap: 12px; }
  .brand-dot { width: 30px; height: 30px; border-radius: 50%; background: var(--brand-blue); }
  .brand-name { font-family: "Fredoka", sans-serif; font-weight: 500; font-size: 66px; line-height: 1; color: var(--brand-blue); letter-spacing: -1px; }
  .announce { position: absolute; left: 456px; top: 76px; font-family: "Fredoka", sans-serif; font-weight: 600; }
  .announce-lead { display: block; color: var(--paper); font-size: 22px; line-height: 28px; }
  .announce-main { display: block; color: var(--brand-blue); font-size: 29px; line-height: 36px; text-transform: uppercase; }

  .photo { position: absolute; left: 44px; width: 396px; }
  .photo-laptop { top: 214px; height: 298px; background: linear-gradient(135deg, #e8e6e3 0%, #d9d3cf 45%, #b05a5e 75%, #e9e9ea 100%); }
  .photo-tablet { top: 526px; height: 268px; background: linear-gradient(120deg, #4a4c48 0%, #7a7d78 40%, #d8d4d0 60%, #3f423f 100%); }
  .photo-kids { top: 807px; height: 268px; background: linear-gradient(100deg, #f1efe9 0%, #e6e2da 45%, #b9c0cc 75%, #e8e8e8 100%); }

  .heading { position: absolute; left: 466px; font-family: "Fredoka", sans-serif; font-weight: 600; font-size: 29px; line-height: 1; color: var(--ink); text-transform: uppercase; }
  .services-heading { top: 220px; }
  .service-list { position: absolute; left: 488px; top: 276px; list-style: none; }
  .service-list li { position: relative; padding-left: 20px; font-size: 25px; line-height: 55.6px; color: var(--text); }
  .service-list li::before { content: ""; position: absolute; left: 0; top: 26px; width: 6px; height: 6px; border-radius: 50%; background: var(--text); }

  .plans-heading { top: 650px; font-size: 27px; }
  .price { position: absolute; left: 466px; top: 686px; font-family: "Fredoka", sans-serif; font-weight: 600; font-size: 56px; line-height: 1; color: var(--brand-blue); }
  .call-heading { top: 794px; font-size: 27px; }
  .phone { position: absolute; left: 466px; top: 830px; font-family: "Fredoka", sans-serif; font-weight: 600; font-size: 56px; line-height: 1; color: var(--brand-blue); }

  .address-block { position: absolute; left: 466px; top: 963px; width: 266px; height: 107px; border: 1px solid #444; font-family: "Arimo", sans-serif; }
  .route-code { position: absolute; right: 20px; top: 12px; font-size: 12px; }
  .recipient { position: absolute; left: 19px; top: 56px; font-size: 15px; line-height: 18px; }
  .indicia { position: absolute; left: 738px; top: 963px; width: 80px; height: 80px; border: 1px solid #444; font-family: "Arimo", sans-serif; font-size: 10.5px; line-height: 13px; text-align: center; padding-top: 5px; }
  .indicia strong { font-weight: 700; }

  .footer-band { position: absolute; left: 0; top: 1102px; width: 934px; height: 98px; }
  .footer-text { position: absolute; left: 54px; top: 1131px; font-family: "Fredoka", sans-serif; font-weight: 500; font-size: 22px; color: var(--paper); letter-spacing: 0.6px; }
</style>
</head>
<body>
<main class="mailer">
  <header class="masthead">
    <div class="brand"><span class="brand-dot"></span><span class="brand-name">Quarvena</span></div>
    <p class="announce">
      <span class="announce-lead">Quarvena Broadband Services are</span>
      <span class="announce-main">Available in your area!</span>
    </p>
  </header>

  <div class="photo photo-laptop" role="img" aria-label="Stock photo of a smiling man in a plaid shirt using a laptop at a home desk"></div>
  <div class="photo photo-tablet" role="img" aria-label="Stock photo of a smiling woman with curly hair using a tablet"></div>
  <div class="photo photo-kids" role="img" aria-label="Stock photo of two laughing children looking at a phone on a sofa"></div>

  <h2 class="heading services-heading">Our Services</h2>
  <ul class="service-list">
    <li>24/7 Technical Support</li>
    <li>Flat Monthly Rates</li>
    <li>No Data Caps</li>
    <li>No Speed Throttling</li>
    <li>No Long Term Contracts</li>
    <li>No Installation Fees</li>
  </ul>

  <h2 class="heading plans-heading">Internet Plans Start At</h2>
  <p class="price">$39.95/mo</p>
  <h2 class="heading call-heading">Call Today</h2>
  <p class="phone">555-304-8926</p>

  <div class="address-block">
    <span class="route-code">****************ECRWSS****</span>
    <p class="recipient">Local<br>Postal Customer</p>
  </div>
  <div class="indicia">PRSRT STD<br>ECRWSS<br>U.S. Postage<br><strong>PAID</strong><br>TRPL RETAIL</div>

  <svg class="footer-band" width="934" height="98" viewBox="0 0 934 98" aria-hidden="true">
    <polygon points="0,0 756,0 716,98 0,98" fill="var(--ink)"/>
    <polygon points="772,0 934,0 934,98 730,98" fill="var(--brand-blue)"/>
  </svg>
  <p class="footer-text">Visit our us at www.quarvena.co for more information</p>
</main>
</body>
</html>
```